Private Investment Firm Needs PowerPoint Presentation Template

Design PowerPoint template, take Ridgeholm-submitted rough presentation draft, and drop it into new template. See attached Project Brief file for more detail.
Updates

Some decent designs have been submitted but they seem to lack the understanding of our target markets. I am hopeful that more time and feedback will result in better results.

Target Market(s)

Private company owners and intermediaries.

Font styles to use
Serif

Colors
3176b5

Requirements
Must have
• See attached Project Brief.
Nice to have
Should not have
• No B2C fluff--this is a B2B project.

```html
<!DOCTYPE html>
<html lang="en">
<head>
<meta charset="utf-8">
<title>Ridgeholm – Firm Overview Template</title>
<link href="https://fonts.googleapis.com/css2?family=Arimo:wght@400;700&display=swap" rel="stylesheet">
<style>
:root{
  --canvas:#ececec;
  --brand:#3176b5;
  --navy:#2a5682;
  --navy-deep:#1f4168;
  --ink:#3a3a3a;
  --muted:#666;
  --rule:#c9c9c9;
  --white:#fff;
}
*{box-sizing:border-box;margin:0;padding:0}
html,body{width:1200px;height:1050px;overflow:hidden;background:var(--canvas);font-family:"Arimo",Arial,sans-serif;color:var(--ink)}
.canvas{position:relative;width:1200px;height:1050px}
.slide{position:absolute;width:555px;height:313px;background:var(--white);overflow:hidden}
.abs{position:absolute}
.brandmark{position:absolute;display:flex;align-items:center;gap:5px}
.brandmark .dot{width:9px;height:9px;background:var(--brand)}
.brandmark .name{font-size:10px;font-weight:700;letter-spacing:1.5px;color:var(--navy);line-height:1}
.brandmark .sub{font-size:5px;letter-spacing:2px;color:var(--navy);display:block;margin-top:2px}
.brandmark.light .dot{background:var(--white)}
.brandmark.light .name,.brandmark.light .sub{color:var(--white)}
.slide-title{position:absolute;left:18px;font-size:17px;color:#404040}
.title-rule{position:absolute;height:1px;background:var(--rule)}
.footer{position:absolute;left:0;bottom:0;width:555px;height:18px}

/* cover */
.cover{left:22px;top:14px;background:linear-gradient(180deg,#2c5582 0%,#335f8d 55%,#2a4f78 100%)}
.cover .skyline{position:absolute;left:0;top:0;width:555px;height:313px;background:linear-gradient(180deg,rgba(255,255,255,0) 30%,rgba(255,255,255,.07) 55%,rgba(10,30,60,.15) 100%)}
.cover h1{position:absolute;left:210px;top:146px;font-size:34px;color:var(--white);font-weight:700}
.cover .underline{position:absolute;left:232px;top:193px;width:133px;height:2px;background:var(--white)}

/* what we do */
.whatwedo{left:619px;top:14px}
.band{position:absolute;left:0;top:72px;width:555px;height:90px;background:var(--navy)}
.band h2{text-align:center;margin-top:16px;font-size:15px;color:var(--white);font-weight:400}
.pillar-icon{position:absolute;width:66px;height:66px;border-radius:50%;background:var(--white);border:2px solid var(--brand);display:flex;align-items:center;justify-content:center}
.pillar-text{position:absolute;top:206px;width:118px;text-align:center;font-size:8.5px;line-height:1.3;color:#505050}
.pillar-divider{position:absolute;top:178px;width:1px;height:84px;background:#ddd}

/* portfolio */
.portfolio{left:22px;top:335px}
.portfolio .slide-title{top:9px;font-size:15px;line-height:1.15;font-weight:700;color:#3b3b3b}
.deal{position:absolute;width:260px;height:62px}
.deal .logo{position:absolute;left:0;top:4px;width:66px;font-size:9px;font-weight:700;color:var(--navy);display:flex;align-items:center;gap:3px}
.deal .logo .dot{width:6px;height:6px;background:var(--brand);flex:none}
.deal .body{position:absolute;left:72px;top:0;width:178px}
.deal h3{font-size:7px;font-weight:700;color:var(--brand);margin-bottom:3px}
.deal ul{list-style:disc;padding-left:6px}
.deal li{font-size:4.2px;line-height:1.3;color:#555;margin-bottom:1px}
.deal-rule{position:absolute;height:1px;background:#e2e2e2}

/* criteria */
.criteria{left:619px;top:335px}
.criteria h2{position:absolute;left:17px;top:60px;width:265px;font-size:12px;line-height:1.25;font-weight:700;color:var(--brand)}
.checklist{position:absolute;left:17px;top:100px;list-style:none}
.checklist li{display:flex;align-items:center;height:25.2px;font-size:8px;color:#444}
.checklist svg{margin-right:9px;flex:none}
.checklist b{color:var(--brand)}
.criteria .photo{position:absolute;left:298px;top:48px;width:257px;height:225px;background:linear-gradient(135deg,#54606e 0%,#a9b6c4 45%,#e4e8ed 70%,#6b7683 100%)}

/* contact */
.contact{left:22px;top:658px;height:315px;background:var(--navy)}
.contact .topbar{position:absolute;left:0;top:0;width:555px;height:48px;background:var(--white)}
.contact .portrait{position:absolute;left:18px;top:48px;width:205px;height:267px;background:linear-gradient(180deg,#d8dadb 0%,#c9ccce 45%,#5d7fb3 75%,#4a6fa8 100%)}
.contact h2{position:absolute;left:240px;top:70px;font-size:21px;color:var(--white);font-weight:700}
.contact .block{position:absolute;font-size:9.5px;line-height:12.6px;color:var(--white)}
.contact .block strong{font-size:10px}
.contact a{color:var(--white)}

.caption{position:absolute;left:18px;top:990px;font-size:43px;font-weight:700;color:var(--navy)}
</style>
</head>
<body>
<div class="canvas">

  <!-- Cover -->
  <section class="slide cover">
    <div class="skyline" role="img" aria-label="Faded city skyline photograph over water in blue tones"></div>
    <div class="brandmark light" style="right:22px;top:22px"><span class="dot"></span><span><span class="name">RIDGEHOLM</span><span class="sub">CAPITAL</span></span></div>
    <h1>Firm Overview</h1>
    <div class="underline"></div>
  </section>

  <!-- What we do -->
  <section class="slide whatwedo">
    <div class="slide-title" style="top:21px">What We Do / and Why</div>
    <div class="brandmark" style="right:18px;top:16px"><span class="dot"></span><span><span class="name">RIDGEHOLM</span><span class="sub">CAPITAL</span></span></div>
    <div class="title-rule" style="left:18px;top:47px;width:519px"></div>
    <div class="band"><h2>Non-control Capital Transactions Only</h2></div>

    <div class="pillar-icon" style="left:43px;top:128px">
      <svg width="34" height="34" viewBox="0 0 34 34" fill="none" stroke="#3176b5" stroke-width="1.6" stroke-linejoin="round"><path d="M3 12l6-5 8 5 8-5 6 5-13 13z"/><path d="M11 17l4 4M14 14l5 5M17 12l5 5"/></svg>
    </div>
    <div class="pillar-icon" style="left:178px;top:128px">
      <svg width="34" height="34" viewBox="0 0 34 34" fill="none" stroke="#3176b5" stroke-width="1.6"><path d="M8 4h14l5 5v21H8z"/><path d="M12 11h8M12 15h6M12 19h4"/><circle cx="22" cy="22" r="4"/><path d="M22 16v2M22 26v2M16 22h2M26 22h2"/></svg>
    </div>
    <div class="pillar-icon" style="left:312px;top:128px">
      <svg width="34" height="34" viewBox="0 0 34 34" fill="none" stroke="#3176b5" stroke-width="1.6"><rect x="4" y="10" width="26" height="18" rx="2"/><path d="M12 10V6h10v4M4 17h26M15 17v3h4v-3"/></svg>
    </div>
    <div class="pillar-icon" style="left:446px;top:128px">
      <svg width="34" height="34" viewBox="0 0 34 34" fill="none" stroke="#3176b5" stroke-width="1.6"><path d="M13 5h8l-3 5h-2z"/><path d="M15 10C7 14 6 28 17 29c11-1 10-15 2-19z"/><path d="M19.5 16.5c-1-1-5-1-5 1.2s5 1.3 5 3.6-4 2.3-5.2 1M17 14.5v10"/></svg>
    </div>

    <p class="pillar-text" style="left:17px">Companies looking for a partner to help them grow, not sellers looking to exit</p>
    <div class="pillar-divider" style="left:143px"></div>
    <p class="pillar-text" style="left:152px">Management's personal wealth directly tied to the performance of the investment</p>
    <div class="pillar-divider" style="left:278px"></div>
    <p class="pillar-text" style="left:286px">Situational investors with a generalist approach</p>
    <div class="pillar-divider" style="left:412px"></div>
    <p class="pillar-text" style="left:420px">Our heritage reflects decades of Non-Control Capital investing—it's all we do</p>

    <svg class="footer" viewBox="0 0 555 18"><rect x="0" y="4" width="500" height="14" fill="#3176b5"/><polygon points="460,4 500,4 518,18 478,18" fill="#1f4168"/><rect x="12" y="7" width="6" height="8" fill="#fff"/><rect x="23" y="7" width="0.6" height="8" fill="#fff"/><text x="27" y="13.5" font-size="5" fill="#fff" font-family="Arimo,sans-serif">Confidential</text><text x="538" y="12" font-size="6" fill="#555" font-family="Arimo,sans-serif">8</text></svg>
  </section>

  <!-- Portfolio -->
  <section class="slide portfolio">
    <div class="slide-title">Ridgeholm Representative<br>Non-Control Capital Investments</div>
    <div class="brandmark" style="right:18px;top:16px"><span class="dot"></span><span><span class="name">RIDGEHOLM</span><span class="sub">CAPITAL</span></span></div>
    <div class="title-rule" style="left:18px;top:47px;width:519px"></div>

    <div class="deal" style="left:18px;top:66px">
      <div class="logo"><span class="dot"></span>Veltra Air</div>
      <div class="body"><h3>Growth Capital</h3><ul>
        <li>Operates dedicated commercial pilot training centers across the region, with classrooms, procedures trainers and full motion simulators.</li>
        <li>Ridgeholm capital funded the near term growth plan, supported recruiting of management and the opening of a new training center.</li></ul></div>
    </div>
    <div class="deal-rule" style="left:18px;top:122px;width:248px"></div>
    <div class="deal" style="left:18px;top:136px">
      <div class="logo"><span class="dot"></span>Quellon</div>
      <div class="body"><h3>Acquisition Finance</h3><ul>
        <li>Manufacturer of vibration isolation, seismic control and shock protection products that limit damage to sensitive equipment.</li>
        <li>Ridgeholm capital was used to acquire two add-on companies that expanded reach; three years later the company set a record.</li></ul></div>
    </div>
    <div class="deal-rule" style="left:18px;top:198px;width:248px"></div>
    <div class="deal" style="left:18px;top:206px">
      <div class="logo"><span class="dot"></span>Summit Guard</div>
      <div class="body"><h3>Family Ownership &amp; Wealth Transfer</h3><ul>
        <li>Provider of fire and security alarm design, installation, service and monitoring for commercial and residential customers.</li>
        <li>Ridgeholm capital let the founder transfer ownership to the next generation while management kept control; the family later bought out the position.</li></ul></div>
    </div>

    <div class="deal" style="left:290px;top:66px">
      <div class="logo"><span class="dot"></span>Corvane</div>
      <div class="body"><h3>Management Buy-Out (MBO)</h3><ul>
        <li>Provider of audit compliance software and consulting services for hospitals and physician practices nationwide.</li>
        <li>Ridgeholm capital helped the active CEO acquire the business from an inactive founder and build a leading platform.</li></ul></div>
    </div>
    <div class="deal-rule" style="left:290px;top:126px;width:248px"></div>
    <div class="deal" style="left:290px;top:136px">
      <div class="logo"><span class="dot"></span>Fleetmark</div>
      <div class="body"><h3>Balance Sheet Recapitalization</h3><ul>
        <li>Provider of third party vehicle maintenance services for private, public and fleet based businesses across the country.</li>
        <li>Ridgeholm capital supported accelerating growth with subordinated debt and equity, and the company grew well over three years.</li></ul></div>
    </div>
    <div class="deal-rule" style="left:290px;top:202px;width:248px"></div>
    <div class="deal" style="left:290px;top:214px">
      <div class="logo"><span class="dot"></span>Orlin Corp</div>
      <div class="body"><h3>Family Office Support</h3><ul>
        <li>Provides custom packaging for liquid home cleaning products, with the ability to safely handle bleach and peroxide.</li>
        <li>Ridgeholm capital helped a family office acquire the company as part of its long term growth strategy.</li></ul></div>
    </div>

    <svg class="footer" viewBox="0 0 555 18"><rect x="0" y="4" width="500" height="14" fill="#3176b5"/><polygon points="460,4 500,4 518,18 478,18" fill="#1f4168"/><rect x="12" y="7" width="6" height="8" fill="#fff"/><rect x="23" y="7" width="0.6" height="8" fill="#fff"/><text x="27" y="13.5" font-size="5" fill="#fff" font-family="Arimo,sans-serif">Confidential</text><text x="533" y="12" font-size="6" fill="#555" font-family="Arimo,sans-serif">9</text></svg>
  </section>

  <!-- Investment criteria -->
  <section class="slide criteria">
    <div class="slide-title" style="top:20px">Investment Criteria</div>
    <div class="brandmark" style="right:18px;top:16px"><span class="dot"></span><span><span class="name">RIDGEHOLM</span><span class="sub">CAPITAL</span></span></div>
    <div class="title-rule" style="left:0;top:47px;width:298px"></div>
    <h2>Ridgeholm invests in established, lower middle market companies.</h2>
    <ul class="checklist">
      <li><svg width="17" height="17" viewBox="0 0 17 17" fill="none" stroke="#3176b5" stroke-width="1.3"><circle cx="8.5" cy="8.5" r="7.6"/><path d="M5 8.7l2.4 2.4 4.6-4.8"/></svg>Revenues of&nbsp;<b>$10MM to $150MM</b></li>
      <li><svg width="17" height="17" viewBox="0 0 17 17" fill="none" stroke="#3176b5" stroke-width="1.3"><circle cx="8.5" cy="8.5" r="7.6"/><path d="M5 8.7l2.4 2.4 4.6-4.8"/></svg>EBITDA of at least&nbsp;<b>$2MM</b></li>
      <li><svg width="17" height="17" viewBox="0 0 17 17" fill="none" stroke="#3176b5" stroke-width="1.3"><circle cx="8.5" cy="8.5" r="7.6"/><path d="M5 8.7l2.4 2.4 4.6-4.8"/></svg>Ridgeholm investment size of&nbsp;<b>$5MM to $25MM</b></li>
      <li><svg width="17" height="17" viewBox="0 0 17 17" fill="none" stroke="#3176b5" stroke-width="1.3"><circle cx="8.5" cy="8.5" r="7.6"/><path d="M5 8.7l2.4 2.4 4.6-4.8"/></svg><span><span style="color:var(--brand)">Experienced, committed,</span> and incented management</span></li>
      <li><svg width="17" height="17" viewBox="0 0 17 17" fill="none" stroke="#3176b5" stroke-width="1.3"><circle cx="8.5" cy="8.5" r="7.6"/><path d="M5 8.7l2.4 2.4 4.6-4.8"/></svg>Limited leverage (aka debt)&nbsp;<b style="color:var(--navy)">“ahead”</b>&nbsp;of Ridgeholm</li>
      <li><svg width="17" height="17" viewBox="0 0 17 17" fill="none" stroke="#3176b5" stroke-width="1.3"><circle cx="8.5" cy="8.5" r="7.6"/><path d="M5 8.7l2.4 2.4 4.6-4.8"/></svg>Niche market leader with&nbsp;<b>differentiated services or products</b></li>
      <li><svg width="17" height="17" viewBox="0 0 17 17" fill="none" stroke="#3176b5" stroke-width="1.3"><circle cx="8.5" cy="8.5" r="7.6"/><path d="M5 8.7l2.4 2.4 4.6-4.8"/></svg>Focused on&nbsp;<b>value-added execution,</b>&nbsp;not proof of concept</li>
    </ul>
    <div class="photo" role="img" aria-label="Photograph of business people reviewing charts on a tablet at a desk"></div>
    <svg class="footer" viewBox="0 0 555 18"><rect x="0" y="4" width="500" height="14" fill="#3176b5"/><polygon points="460,4 500,4 518,18 478,18" fill="#1f4168"/><rect x="12" y="7" width="6" height="8" fill="#fff"/><rect x="23" y="7" width="0.6" height="8" fill="#fff"/><text x="27" y="13.5" font-size="5" fill="#fff" font-family="Arimo,sans-serif">Confidential</text><text x="530" y="12" font-size="6" fill="#555" font-family="Arimo,sans-serif">10</text></svg>
  </section>

  <!-- Contact -->
  <section class="slide contact">
    <div class="topbar"></div>
    <div class="brandmark" style="right:18px;top:16px"><span class="dot"></span><span><span class="name">RIDGEHOLM</span><span class="sub">CAPITAL</span></span></div>
    <div class="portrait" role="img" aria-label="Portrait photograph of the firm principal in a blue shirt"></div>
    <h2>Contact</h2>
    <div class="block" style="left:240px;top:111px">
      <strong>Daniel R. Ashworth</strong><br>Principal<br>41 Larchmont Ridge Road,<br>Suite 210<br>Easton, CT&nbsp; 06612<br>Direct: (555) 204-7731<br><a href="mailto:dashworth@ridgeholmcapital.example">dashworth@ridgeholmcapital.example</a>
    </div>
    <div class="block" style="left:401px;top:111px">
      <strong>San Francisco Office</strong><br>Two Harbor Lane, Suite 400<br>San Francisco, CA 94111<br>(555) 310-4820
    </div>
    <div class="block" style="left:240px;top:212px">
      <strong>Boston Office</strong><br>18 Millbrook Drive, Suite 300<br>Beverly, MA 01915<br>(555) 204-7700
    </div>
    <div class="block" style="left:240px;top:276px">www.ridgeholmcapital.example</div>
  </section>

  <div class="caption">Ridgeholm - Second Part</div>
</div>
</body>
</html>
```